"Pause. Pivot. Prosper." Empowerment Book Cover

Hello, I need a hot, trendy, and contemporary book cover designed for my first book called "Pause. Pivot. Prosper. -- 365 Bold Confidence Notes for Anyone Seeking to Pause, Pivot, and Prosper Across Career & Personal Dreams."
This is my first book and I am really wanting to launch my brand with it... it would be awesome to match the inside/outside branding of the book. So we can either create the book cover to match the book guts, or update the book guts to match the cover.
Lastly, I just got a professional photoshoot done last week so we can use one of those images, or we can go with a different idea/style for the cover. The body of the book is attached. All questions welcomed, happy designing!
Target Market(s)
Gen Z, Millennials and Gen X.
Industry/Entity Type
Personal Development.
Requirements
Must have
- It must stand out and be different from other typical book covers.
Nice to have
- Success, Inspiration, Motivation, Mindset, Growth.
Should not have
- Clipart, stock art, stock look and feel.

```html
<!DOCTYPE html>
<html lang="en">
<head>
<meta charset="UTF-8">
<title>Pause. Pivot. Prosper. — Book Cover</title>
<link rel="stylesheet" href="https://fonts.googleapis.com/css2?family=Questrial&display=swap">
<style>
  :root {
    --page-bg: #ffffff;
    --sky-top: #9aa8b3;
    --sky-mid: #4f6a86;
    --navy-deep: #0c2a55;
    --navy-base: #0a2349;
    --title-one: #1ba6dd;
    --title-two: #62c2e4;
    --title-three: #c4e6f2;
    --text-light: #eef3f7;
  }
  * { margin: 0; padding: 0; box-sizing: border-box; }
  html, body {
    width: 1200px;
    height: 1200px;
    overflow: hidden;
    background: var(--page-bg);
    font-family: "Questrial", "Century Gothic", sans-serif;
  }
  .book-cover {
    position: absolute;
    left: 220px;
    top: 30px;
    width: 760px;
    height: 1140px;
    overflow: hidden;
  }
  .cover-portrait {
    position: absolute;
    inset: 0;
    background:
      radial-gradient(ellipse 70% 45% at 75% 30%, rgba(190, 202, 212, 0.55), transparent 70%),
      linear-gradient(180deg, var(--sky-top) 0%, var(--sky-mid) 38%, var(--navy-deep) 70%, var(--navy-base) 100%);
  }
  .cover-subtitle {
    position: absolute;
    left: 345px;
    top: 140px;
    width: 390px;
    color: var(--text-light);
    font-size: 28px;
    line-height: 1.38;
    letter-spacing: 0.2px;
  }
  .cover-title {
    position: absolute;
    left: 52px;
    top: 535px;
    font-weight: 400;
    line-height: 1;
  }
  .cover-title span {
    display: block;
    font-size: 146px;
    letter-spacing: -2px;
    text-shadow: 0 3px 8px rgba(0, 0, 0, 0.35);
  }
  .title-pause   { color: var(--title-one); }
  .title-pivot   { color: var(--title-two); margin-top: 30px; }
  .title-prosper { color: var(--title-three); margin-top: 30px; }
  .cover-author {
    position: absolute;
    left: 56px;
    top: 1040px;
    color: var(--text-light);
    font-size: 46px;
    letter-spacing: 0.5px;
  }
</style>
</head>
<body>
  <main class="book-cover">
    <div class="cover-portrait" role="img" aria-label="Portrait photo of the author in a navy suit jacket and white shirt against a soft grey-blue backdrop"></div>
    <p class="cover-subtitle">365 Bold Confidence Notes for Anyone Seeking to Pause, Pivot, and Prosper Across Career &amp; Personal Dreams.</p>
    <h1 class="cover-title">
      <span class="title-pause">Pause.</span>
      <span class="title-pivot">Pivot.</span>
      <span class="title-prosper">Prosper.</span>
    </h1>
    <p class="cover-author">Daniel Okafor</p>
  </main>
</body>
</html>
```